Thornbury Ridge & Beam Consultants- WEB DESIGN

I am seeking a more professional face to my current website.

www.TRBconsultants.com.au

Using same pages and same text, i need the pages to be presented in a more professional manner.

Use Same logo however all other items may be changed to make it look better... Main theme being a navy blue.

Project Deadline Extended
Reason: Alot of recent interest. Awaiting designs.

Target Market(s)

Engineers, Students, Public, Local Authorities, Draftsmen, Architects, Builders etc

Requirements
Must have
• Logo as per site,
• Navy Blue Theme,
• Professional feel,
• Images to attract eye and clients attention. (dont use large infrastructure yet more Residential designs, Crack inspections and Residential Construction)

```html
<!DOCTYPE html>
<html lang="en">
<head>
<meta charset="utf-8">
<title>Thornbury Ridge &amp; Beam Consultants</title>
<link href="https://fonts.googleapis.com/css2?family=Raleway:wght@400;500&family=Noto+Sans:wght@400&display=swap" rel="stylesheet">
<style>
:root{
  --navy:#0a3f66;
  --navy-band:#1d5884;
  --navy-line:#0e3552;
  --brand-blue:#2c3f9b;
  --ink:#111;
  --white:#fff;
  --panel:rgba(60,55,50,.72);
  --field:rgba(235,235,235,.85);
  --members-bg:#f2f2f2;
  --badge-blue:#1688e0;
  --badge-red:#e4291f;
}
*{box-sizing:border-box;margin:0;padding:0}
html,body{width:1138px;height:1200px;overflow:hidden;background:var(--white)}
body{position:relative;font-family:"Noto Sans",Verdana,sans-serif;color:var(--ink)}
.abs{position:absolute}

.site-header{left:0;top:0;width:1138px;height:135px;background:var(--white)}
.brand{left:0;top:76px;width:1138px;text-align:center;font-family:"Raleway",sans-serif;font-weight:500;font-size:19px;letter-spacing:4px;color:var(--brand-blue);text-transform:uppercase}
.brand-mark{left:549px;top:28px;width:40px;height:40px;background:var(--brand-blue)}
.register-tab{left:886px;top:0;width:138px;height:35px;background:var(--navy);border-radius:0 0 10px 10px;color:var(--white);font-family:"Raleway",sans-serif;font-size:16px;text-align:center;line-height:33px;box-shadow:0 2px 3px rgba(0,0,0,.35)}

.service-nav{left:0;top:135px;width:1138px;height:107px;background:linear-gradient(180deg,#24618f,var(--navy-band));border-top:2px solid var(--navy-line)}
.service{top:0;width:227px;height:105px;border-left:1px solid var(--navy-line);color:var(--white);text-align:center;font-family:"Raleway",sans-serif;font-size:12px}
.service svg{position:absolute;left:50%;top:16px;transform:translateX(-50%)}
.service span{position:absolute;left:0;right:0;top:72px}
.nav-end{top:0;left:1023px;height:105px;border-left:1px solid var(--navy-line)}

.hero-photo{left:0;top:242px;width:1138px;height:445px;background:linear-gradient(110deg,#a6582a 0%,#d79a5a 30%,#e6c08b 52%,#c98449 70%,#9aa9b6 88%,#7d93a6 100%)}
.register-panel{left:569px;top:314px;width:455px;height:373px;background:var(--panel)}
.register-title{left:25px;top:22px;font-family:"Raleway",sans-serif;font-size:23px;line-height:26px;color:var(--white);font-weight:400}
.field-label{left:25px;font-family:"Raleway",sans-serif;font-size:17px;line-height:20px;color:var(--white)}
.field{left:179px;width:249px;height:40px;background:var(--field)}
.register-btn{left:-6px;top:320px;width:431px;height:44px;background:#000;clip-path:polygon(0 0,93% 0,100% 50%,93% 100%,0 100%);color:var(--white);font-family:"Raleway",sans-serif;font-size:23px;line-height:45px;padding-left:31px}

.section-rule{top:741px;height:2px;background:var(--ink)}
.section-title{left:0;top:724px;width:1138px;text-align:center;font-family:"Raleway",sans-serif;font-size:28px;font-weight:400;letter-spacing:.5px}
.service-list{list-style:none;font-size:15px;letter-spacing:.4px}
.service-list li{height:26.7px;position:relative;padding-left:26px}
.service-list li svg{position:absolute;left:0;top:3px}

.members{left:0;top:988px;width:1138px;height:143px;background:var(--members-bg)}
.members-title{left:114px;top:54px;font-family:"Raleway",sans-serif;font-size:28px;font-weight:400}

.site-footer{left:0;top:1131px;width:1138px;height:69px;background:var(--navy);color:var(--white);font-size:11px;letter-spacing:.3px}
</style>
</head>
<body>
<header class="site-header abs">
  <div class="brand-mark abs"></div>
  <div class="brand abs">Thornbury Ridge &amp; Beam Consultants</div>
  <div class="register-tab abs">REGISTER</div>
</header>

<nav class="service-nav abs">
  <div class="service abs" style="left:113px">
    <svg width="44" height="46" viewBox="0 0 44 46" fill="none" stroke="#fff" stroke-width="3"><path d="M4 20 22 4 40 20M9 16v26h26V16M16 42V28h12v14"/></svg>
    <span>STRUCTURAL ENGINEERING</span></div>
  <div class="service abs" style="left:340px">
    <svg width="90" height="46" viewBox="0 0 90 46" fill="#fff"><path d="M4 22 22 6 30 12v30H4z"/><rect x="36" y="10" width="30" height="26" rx="10" fill="none" stroke="#fff" stroke-width="3"/><path d="M68 18h10v-4l8 9-8 9v-4H68z"/></svg>
    <span>ENERGY RATING</span></div>
  <div class="service abs" style="left:569px">
    <svg width="70" height="50" viewBox="0 0 70 50" fill="#fff"><path d="M2 22 24 2 46 22H40v26H8V22z"/><rect x="46" y="10" width="12" height="8"/><rect x="48" y="22" width="12" height="8"/><rect x="50" y="34" width="12" height="8"/></svg>
    <span>HOUSE INSPECTIONS</span></div>
  <div class="service abs" style="left:796px">
    <svg width="46" height="48" viewBox="0 0 46 48" fill="none" stroke="#fff" stroke-width="3"><path d="M3 22 23 4 43 22M7 19v26h32V19M7 30h32M15 45V22M31 45V22M15 30 31 45M31 30 15 45"/></svg>
    <span>CONSTRUCTION</span></div>
  <div class="nav-end abs"></div>
</nav>

<section class="hero-photo abs" role="img" aria-label="Photo of two builders in hard hats reading plans inside a timber house frame"></section>
<form class="register-panel abs">
  <h2 class="register-title abs">REGISTER</h2>
  <div class="field-label abs" style="top:63px">Business Name</div><div class="field abs" style="top:53px"></div>
  <div class="field-label abs" style="top:116px">Suburb</div><div class="field abs" style="top:106px"></div>
  <div class="field-label abs" style="top:170px">State</div>
  <div class="field abs" style="top:160px"><svg class="abs" style="right:8px;top:15px" width="16" height="10" viewBox="0 0 16 10"><path d="M1 1 8 8 15 1" stroke="#333" stroke-width="3" fill="none"/></svg></div>
  <div class="field-label abs" style="top:223px">Your Name</div><div class="field abs" style="top:213px"></div>
  <div class="field-label abs" style="top:276px">Phone</div><div class="field abs" style="top:266px"></div>
  <div class="register-btn abs">REGISTER NOW</div>
</form>

<section>
  <div class="section-rule abs" style="left:114px;width:352px"></div>
  <div class="section-rule abs" style="left:673px;width:351px"></div>
  <h2 class="section-title abs">WHAT WE DO</h2>
  <ul class="service-list abs" style="left:123px;top:782px">
    <li><svg width="16" height="14" viewBox="0 0 16 14"><path d="M0 7 8 0l8 7h-2v7H2V7z" fill="#333"/></svg>Structural Design</li>
    <li><svg width="16" height="14" viewBox="0 0 16 14"><path d="M0 7 8 0l8 7h-2v7H2V7z" fill="#333"/></svg>Civil Drainage Design</li>
    <li><svg width="16" height="14" viewBox="0 0 16 14"><path d="M0 7 8 0l8 7h-2v7H2V7z" fill="#333"/></svg>Site Inspections, Crack Inspections</li>
    <li><svg width="16" height="14" viewBox="0 0 16 14"><path d="M0 7 8 0l8 7h-2v7H2V7z" fill="#333"/></svg>Insurance Assessments.</li>
    <li><svg width="16" height="14" viewBox="0 0 16 14"><path d="M0 7 8 0l8 7h-2v7H2V7z" fill="#333"/></svg>Pre-Purchase Home inspections</li>
    <li><svg width="16" height="14" viewBox="0 0 16 14"><path d="M0 7 8 0l8 7h-2v7H2V7z" fill="#333"/></svg>Certificates of Compliance 1507 - Design / Inspection</li>
  </ul>
  <ul class="service-list abs" style="left:578px;top:782px">
    <li><svg width="16" height="14" viewBox="0 0 16 14"><path d="M0 7 8 0l8 7h-2v7H2V7z" fill="#333"/></svg>Retail buildings and shopping centers</li>
    <li><svg width="16" height="14" viewBox="0 0 16 14"><path d="M0 7 8 0l8 7h-2v7H2V7z" fill="#333"/></svg>Industrial buildings</li>
    <li><svg width="16" height="14" viewBox="0 0 16 14"><path d="M0 7 8 0l8 7h-2v7H2V7z" fill="#333"/></svg>Education and Institutional buildings</li>
    <li><svg width="16" height="14" viewBox="0 0 16 14"><path d="M0 7 8 0l8 7h-2v7H2V7z" fill="#333"/></svg>Residential houses and townhouses</li>
    <li><svg width="16" height="14" viewBox="0 0 16 14"><path d="M0 7 8 0l8 7h-2v7H2V7z" fill="#333"/></svg>Construction engineering</li>
    <li><svg width="16" height="14" viewBox="0 0 16 14"><path d="M0 7 8 0l8 7h-2v7H2V7z" fill="#333"/></svg>Existing Condition Reports</li>
  </ul>
</section>

<section class="members abs">
  <h2 class="members-title abs">WE ARE MEMBER OF</h2>
  <svg class="abs" style="left:452px;top:27px" width="64" height="90" aria-label="Member association badge" role="img"><rect width="64" height="90" fill="var(--badge-blue)"/></svg>
  <svg class="abs" style="left:569px;top:37px" width="58" height="60" aria-label="Member association badge" role="img"><rect width="58" height="60" fill="var(--badge-red)"/></svg>
  <svg class="abs" style="left:684px;top:15px" width="82" height="82" aria-label="Registered practitioner badge" role="img"><circle cx="41" cy="41" r="39" fill="none" stroke="#1d4d8a" stroke-width="3"/></svg>
</section>

<footer class="site-footer abs">
  <div class="abs" style="left:114px;top:16px">Register Now &nbsp;| &nbsp;Contact Us</div>
  <div class="abs" style="left:114px;top:37px">© 2013. Thornbury Ridge &amp; Beam Consultants. All Rights Reserved</div>
  <svg class="abs" style="left:956px;top:19px" width="70" height="24"><circle cx="11" cy="12" r="10" fill="#fff"/><circle cx="57" cy="12" r="10" fill="#fff"/></svg>
</footer>
</body>
</html>
```